Corvallin Property Solutions need a business card design

Hello guys. We would need a business card design asap please.
We are a start up property investment business based in London UK specialised in buying, selling, managing and letting properties and helping distressed property owners.
The name of our Business is Corvallin, the logo symbolises the four fundamental elements of the world (earth, air, fire and water) and so it stands for strength, stability, longevity.
We would like the business card to communicate professionalism and reliability. Many many thanks indeed for your work.

Details:

1.) Marisol Dunkley
Property Investor
Mobile: +44(0)7700362517
Email: marisol.corvallin@quilbrook.example

2.) Tomas Brindle
Property Investor
Mobile: +44(0)7700845926
Email: tomas.corvallin@quilbrook.example

Industry/Entity Type

Investment

```html
<!DOCTYPE html>
<html lang="en">
<head>
<meta charset="utf-8">
<title>Corvallin Property Solutions – Business Card</title>
<link rel="stylesheet" href="https://fonts.googleapis.com/css2?family=Jost:wght@700&family=Ubuntu:wght@300;400;700&display=swap">
<style>
  :root {
    --backdrop: #222222;
    --card: #ffffff;
    --ink: #111111;
    --ink-soft: #555555;
    --ink-muted: #6f6f6f;
    --red: #c7283a;
    --green: #1d7a3c;
    --blue: #3b6fc6;
    --red-soft: #e4586a;
    --green-soft: #2fa356;
    --blue-soft: #6f9ad8;
  }
  * { margin: 0; padding: 0; box-sizing: border-box; }
  html, body {
    width: 1200px;
    height: 1000px;
    overflow: hidden;
    background: var(--backdrop);
  }
  .stage {
    position: relative;
    width: 1200px;
    height: 1000px;
  }
  .card {
    position: absolute;
    width: 520px;
    height: 300px;
    background: var(--card);
    border-radius: 16px;
    overflow: hidden;
  }

  /* Front: brand face */
  .card--brand { left: 50px; top: 420px; }
  .brand-lockup {
    position: absolute;
    left: 0; right: 0;
    top: 86px;
    display: flex;
    justify-content: center;
    align-items: center;
    gap: 14px;
  }
  .brand-square {
    width: 36px;
    height: 36px;
    background: var(--green);
  }
  .brand-name {
    font-family: "Jost", sans-serif;
    font-weight: 700;
    font-size: 40px;
    letter-spacing: 1px;
    color: var(--ink);
    line-height: 1;
  }
  .brand-tagline {
    position: absolute;
    left: 0; right: 0;
    top: 142px;
    text-align: center;
    font-family: "Jost", sans-serif;
    font-weight: 700;
    font-size: 15px;
    letter-spacing: 0.5px;
    color: var(--ink);
  }
  .colour-rule {
    position: absolute;
    left: 0; right: 0;
    top: 196px;
    display: flex;
    gap: 6px;
    height: 6px;
  }
  .colour-rule span { flex: 1; }
  .colour-rule .red { background: var(--red); }
  .colour-rule .green { background: var(--green); }
  .colour-rule .blue { background: var(--blue); }
  .brand-url {
    position: absolute;
    left: 0; right: 0;
    top: 222px;
    text-align: center;
    font-family: "Ubuntu", sans-serif;
    font-weight: 400;
    font-size: 16px;
    letter-spacing: 1px;
    color: var(--ink-muted);
  }

  /* Back: contact face */
  .card--contact { left: 630px; top: 180px; }
  .corner-graphic {
    position: absolute;
    left: 0; top: 0;
    width: 520px;
    height: 300px;
  }
  .edge-tabs {
    position: absolute;
    left: 0; top: 38px;
    width: 10px;
  }
  .edge-tabs span { display: block; height: 18px; margin-bottom: 3px; }
  .edge-tabs .red { background: var(--red); }
  .edge-tabs .green { background: var(--green); }
  .edge-tabs .blue { background: var(--blue); }
  .contact-name {
    position: absolute;
    left: 44px; top: 40px;
    font-family: "Ubuntu", sans-serif;
    font-weight: 700;
    font-size: 20px;
    color: var(--ink);
  }
  .contact-role {
    position: absolute;
    left: 44px; top: 66px;
    font-family: "Ubuntu", sans-serif;
    font-weight: 300;
    font-size: 13px;
    color: var(--ink-soft);
  }
  .contact-details {
    position: absolute;
    left: 44px; top: 100px;
    font-family: "Ubuntu", sans-serif;
    font-weight: 400;
    font-size: 13px;
    line-height: 18px;
    color: var(--ink-soft);
    list-style: none;
  }
  .contact-url {
    position: absolute;
    left: 44px; bottom: 40px;
    font-family: "Ubuntu", sans-serif;
    font-weight: 400;
    font-size: 14px;
    letter-spacing: 1px;
    color: var(--ink-muted);
  }
</style>
</head>
<body>
  <main class="stage">
    <section class="card card--brand" aria-label="Business card front">
      <div class="brand-lockup">
        <span class="brand-square" aria-hidden="true"></span>
        <h1 class="brand-name">CORVALLIN</h1>
      </div>
      <p class="brand-tagline">PROPERTY SOLUTIONS</p>
      <div class="colour-rule"><span class="red"></span><span class="green"></span><span class="blue"></span></div>
      <p class="brand-url">www.corvallin.com</p>
    </section>

    <section class="card card--contact" aria-label="Business card back">
      <svg class="corner-graphic" viewBox="0 0 520 300" role="img" aria-label="Large brand graphic in red, green and blue filling the lower right corner">
        <defs>
          <linearGradient id="cornerTones" x1="0" y1="1" x2="1" y2="0">
            <stop offset="0" stop-color="var(--green)"/>
            <stop offset="0.4" stop-color="var(--green-soft)"/>
            <stop offset="0.65" stop-color="var(--blue-soft)"/>
            <stop offset="1" stop-color="var(--red-soft)"/>
          </linearGradient>
        </defs>
        <polygon points="210,300 520,62 520,300" fill="url(#cornerTones)"/>
      </svg>
      <div class="edge-tabs"><span class="red"></span><span class="green"></span><span class="blue"></span></div>
      <h2 class="contact-name">Marisol Dunkley</h2>
      <p class="contact-role">Property Investor</p>
      <ul class="contact-details">
        <li>+44(0)7700362517</li>
        <li>marisol.corvallin@quilbrook.example</li>
      </ul>
      <p class="contact-url">www.corvallin.com</p>
    </section>
  </main>
</body>
</html>
```